Sol Gorditas Digital Menu Boards

IF SELECTED, WINNER MAY BE HIRED FOR OTHER DESIGNS OF DIFFERENT STORES OF OUR COMPANY.

Task: Digital Menu Boards Design

Task description: We need designs for a Digital Menu to be displayed on two 42’’screens at Solgorditas, a fast-food restaurant in Guadalajara, Mexico. The menu redesign should communicate to our customers the experience of eating at our restaurant.

For avoiding the creation of videos, we are expecting several menu slides with the same text but with different images, simulating the effect of a video where the images are changing. This menu slides will be projected through a USB memory and a slideshow.

Attached files:
For the design, there are several documents attached to the task description:
1. Logo of the restaurant
2. Pictures of the restaurant
3. Example video of what we want to achieve through this menu slides.
4. Pictures of the actual menu board, to be replaced with the new designs.
5. Menu description (regular and breakfast menu)
6. Pictures of each element on the menu (We don’t have yet any breakfast pictures)
**The files are organized on a ZIP file.

Expected product:
For the regular menu,
• 2 menu slide designs for TACOS Y ESPECIALIDADES, where the text will be exactly the same but the images would differ.
• 2 menu slide designs for BEBIDAS Y EXTRAS, where the text will be exactly the same but the images would differ.
For the breakfast menu,
• 1 menu slide including all the menu
Total: 5 menu board slides.

Technical specs:
• You should send the editable file, med and high resolution JPGs for each design.
• The designs should fit perfectly on 42’’ screens.

```html
<!DOCTYPE html>
<html lang="es">
<head>
<meta charset="UTF-8">
<title>Sol Gorditas – Menú Desayunos</title>
<link rel="stylesheet" href="https://fonts.googleapis.com/css2?family=Bebas+Neue&family=Oswald:wght@500;700&display=swap">
<style>
  :root {
    --stage: #ffffff;
    --cream: #fcf3e0;
    --ink: #1c1a19;
    --label-text: #ffffff;
    --rule: #3a3633;
    --brand-red: #b3202a;
    --badge: #f2d9a4;
    --photo-a: #e9c89a;
    --photo-b: #a2452c;
    --photo-c: #6b3a24;
  }
  * { box-sizing: border-box; margin: 0; padding: 0; }
  html, body {
    width: 1200px; height: 804px; overflow: hidden;
    background: var(--stage);
  }
  .menu-board {
    position: absolute; left: 0; top: 64px;
    width: 1200px; height: 675px;
    background: var(--cream);
    overflow: hidden;
    font-family: "Oswald", sans-serif;
    color: var(--ink);
  }
  .footer-band {
    position: absolute; left: 0; right: 0; bottom: 0; height: 70px;
    background: var(--ink);
  }
  .dish-photo {
    position: absolute; left: 22px; top: 62px; width: 330px; height: 262px;
    border-radius: 46px;
    background: var(--cream);
    border: 2px dotted var(--ink);
    padding: 12px;
  }
  .dish-photo-fill {
    width: 100%; height: 100%; border-radius: 36px;
    background: radial-gradient(ellipse at 40% 55%, var(--photo-b) 0%, var(--photo-a) 55%, var(--photo-c) 100%);
  }
  .tag {
    position: absolute;
    background: var(--ink);
    color: var(--label-text);
    font-family: "Bebas Neue", sans-serif;
    text-align: center;
    letter-spacing: 1px;
  }
  .tag::after {
    content: ""; position: absolute; inset: 5px;
    border-top: 2px dotted var(--label-text);
    border-bottom: 2px dotted var(--label-text);
    opacity: .7;
  }
  .tag-quesadillas {
    left: 40px; top: 342px; width: 288px; height: 52px;
    font-size: 40px; line-height: 54px;
  }
  .tag-desayunos {
    left: 490px; top: 158px; width: 562px; height: 84px;
    font-size: 62px; line-height: 88px;
  }
  .brand {
    position: absolute; left: 40px; top: 470px;
    display: flex; align-items: center; gap: 14px;
  }
  .brand-dot {
    width: 110px; height: 110px; border-radius: 50%;
    background: var(--badge);
    border: 6px solid var(--label-text);
  }
  .brand-name {
    font-family: "Oswald", sans-serif; font-weight: 700;
    font-size: 44px; color: var(--brand-red);
  }
  .price-table {
    position: absolute; left: 430px; top: 272px; width: 700px;
    border-collapse: collapse;
    font-weight: 500;
  }
  .price-table th {
    font-size: 19px; font-weight: 500; height: 40px; text-align: center;
  }
  .price-table td {
    font-size: 21px; height: 45px; text-align: center;
    border-bottom: 2px dotted var(--rule);
  }
  .price-table td.item { text-align: left; font-weight: 700; width: 150px; }
</style>
</head>
<body>
<main class="menu-board">
  <div class="dish-photo">
    <div class="dish-photo-fill" role="img" aria-label="Fotografía de quesadillas con carne, queso y guacamole"></div>
  </div>
  <div class="tag tag-quesadillas">Quesadillas</div>

  <div class="brand">
    <span class="brand-dot"></span>
    <span class="brand-name">Sol Gorditas</span>
  </div>

  <h1 class="tag tag-desayunos">Desayunos</h1>

  <table class="price-table">
    <thead>
      <tr><th></th><th>CHILAQUILES</th><th>BURRITOS</th><th>TACOS DORADOS (3)</th></tr>
    </thead>
    <tbody>
      <tr><td class="item">PASTOR</td><td>$40</td><td>$45</td><td>$40</td></tr>
      <tr><td class="item">ARRACHERA</td><td>$50</td><td>$45</td><td>$45</td></tr>
      <tr><td class="item">QUESO</td><td></td><td>$45</td><td></td></tr>
      <tr><td class="item">HUEVO</td><td></td><td>$45</td><td></td></tr>
    </tbody>
  </table>

  <div class="footer-band"></div>
</main>
</body>
</html>
```